Business Card Design

I need a business card for my tutoring service. Key elements on front are its contact details and visual appeal with these three points: All aspects of literacy and numeracy, 'Bright Pathways Support' provider and Prep-readiness sessions
Updates

contact me by email on korawen7@mailtrove.net as I'm having issues with other address at times. Thanks

:) 

Target Market(s)

People with children

Industry/Entity Type

Tutoring

Contact Information for Business Card

Tessa Brindle Educational Consultant
17 Quillon Grove
Tarrowin 4821
0487 316 912

Requirements
Nice to have
• Something related to education. On the back of the card, my business name and phone number again, along with: spelling, reading, writing, comprehension, oral language, listening skills

```html
<!DOCTYPE html>
<html lang="en">
<head>
<meta charset="utf-8">
<title>Tessa Brindle – Business Card</title>
<link rel="stylesheet" href="https://fonts.googleapis.com/css2?family=Kalam:wght@400&family=Open+Sans:wght@400;600&display=swap">
<style>
  :root {
    --backdrop: #d9dadc;
    --card: #0b0b0b;
    --card-edge: #1c1c1c;
    --gold: #e3a92b;
    --ink: #f4f4f4;
    --rule: #6d6d6d;
  }
  * { box-sizing: border-box; margin: 0; padding: 0; }
  html, body {
    width: 1200px; height: 968px; overflow: hidden;
    background: var(--backdrop);
    font-family: "Open Sans", Arial, sans-serif;
    color: var(--ink);
  }
  .card {
    position: absolute;
    width: 600px; height: 343px;
    background: radial-gradient(ellipse at 45% 35%, var(--card-edge), var(--card) 70%);
    box-shadow: 0 10px 28px rgba(0,0,0,.35);
  }
  .card--back { left: 540px; top: 90px; }
  .card--front { left: 70px; top: 500px; }

  .name {
    font-family: "Kalam", "Comic Sans MS", cursive;
    color: var(--gold);
    font-size: 48px;
    line-height: 1;
    letter-spacing: 1px;
  }

  /* back */
  .back-id {
    position: absolute; left: 0; right: 0; top: 110px;
    text-align: center;
  }
  .back-id .phone {
    display: inline-block;
    margin-top: 6px;
    padding-bottom: 4px;
    border-bottom: 1px solid var(--rule);
    font-size: 12px; letter-spacing: 1px;
  }
  .skills {
    position: absolute; left: 30px; right: 30px; bottom: 40px;
    display: flex; justify-content: space-between; align-items: center;
    list-style: none; font-size: 13px; font-weight: 600;
  }
  .skills .dot {
    width: 5px; height: 5px; border-radius: 50%; background: var(--gold);
  }

  /* front */
  .front-id { position: absolute; left: 68px; top: 70px; }
  .front-id .role {
    display: block; text-align: right; font-size: 13px; margin-top: -2px;
  }
  .services {
    position: absolute; left: 100px; top: 150px;
    list-style: none; font-size: 15px; line-height: 30px;
  }
  .services li:nth-child(1) { padding-left: 24px; }
  .services li:nth-child(2) { padding-left: 4px; }
  .contact {
    position: absolute; left: 375px; top: 232px;
    list-style: none; font-size: 13px; line-height: 22px;
  }
</style>
</head>
<body>

<section class="card card--back" aria-label="Card back">
  <div class="back-id">
    <div class="name">Tessa Brindle</div>
    <div class="phone">4821 0487 316 912</div>
  </div>
  <ul class="skills">
    <li>spelling</li><li class="dot"></li>
    <li>reading</li><li class="dot"></li>
    <li>writing</li><li class="dot"></li>
    <li>comprehension</li><li class="dot"></li>
    <li>oral language</li><li class="dot"></li>
    <li>listening skills</li>
  </ul>
</section>

<section class="card card--front" aria-label="Card front">
  <div class="front-id">
    <div class="name">Tessa Brindle</div>
    <span class="role">Educational Consultant</span>
  </div>

  <ul class="services">
    <li>All aspects of literacy and numeracy</li>
    <li>'Bright Pathways Support' provider</li>
    <li>Prep-readiness sessions</li>
  </ul>

  <ul class="contact">
    <li>17 Quillon Grove Tarrowin</li>
    <li>korawen7@mailtrove.net</li>
    <li>4821 0487 316 912</li>
  </ul>
</section>

</body>
</html>
```